Lotus Vale is a new opened business in takapuna, Auckland, which provide traditional Chinese Therapeutic & relaxation massage. We like to invite more and more people as our customers, especially for the office people near by in the same suburb. We want this flyer to have a pormotion for these kind of people,the probably content of this pormotion is during their lunch break, they will receive a professional Quckily De-stress Relaxation massage for $20 only. We are not the native speaker so we wouldn't use specific sentence to describe. We like the ad be academic and professional.The color we want to use is the same as the file we have attached.also in the flyer we need the direction for the location of our shop.
Massage
Must have
- have a pormotion for office people,the probably content of this pormotion is during their lunch break, they will receive a professional Quckily De-stress Relaxation massage for $20 only.
Nice to have
- our shop address is shop 7, 41 - 55 Brindlecombe Road, Takapuna, Auckland.
Phone number: 09-5317208
Email: lotusvale.nz@examplemail.com
we need the direction for the location of our shop (map)

```html
<!DOCTYPE html>
<html lang="en">
<head>
<meta charset="utf-8">
<title>Lotus Vale – Massage Flyer</title>
<link rel="stylesheet" href="https://fonts.googleapis.com/css2?family=Poppins:wght@600&family=Questrial&family=Arimo:wght@700&display=swap">
<style>
  :root {
    --page-bg: #ffffff;
    --sun: #f6c445;
    --cream: #fff8e6;
    --brown: #5b4119;
    --brown-text: #5a3f14;
    --orange: #f2773a;
    --orange-line: #f29a2e;
    --peach: #f9cdb2;
    --map-yellow: #f7dc4a;
    --map-orange: #f4a13a;
    --white: #ffffff;
  }
  * { margin: 0; padding: 0; box-sizing: border-box; }
  html, body { width: 950px; height: 1200px; overflow: hidden; background: var(--page-bg); }
  .flyer {
    position: absolute; left: 122px; top: 98px; width: 707px; height: 1004px;
    background: linear-gradient(115deg, var(--sun) 0%, #fbdf97 40%, var(--cream) 80%);
    overflow: hidden;
    box-shadow: 0 2px 14px rgba(0,0,0,0.22);
    font-family: "Questrial", "Century Gothic", sans-serif;
    color: var(--brown-text);
  }
  .decor { position: absolute; left: 0; top: 0; width: 707px; height: 1004px; }
  .headline {
    position: absolute; left: 26px; top: 20px;
    font-family: "Poppins", sans-serif; font-weight: 600;
    font-size: 47px; line-height: 58px; color: var(--brown-text);
  }
  .benefit { position: absolute; left: 26px; width: 660px; }
  .benefit h2 {
    font-family: "Poppins", sans-serif; font-weight: 600;
    font-size: 23px; color: var(--orange); line-height: 30px; margin-bottom: 12px;
  }
  .benefit p { font-size: 19.5px; line-height: 20.5px; }
  .benefit--sports { top: 150px; }
  .benefit--remedial { top: 339px; }
  .benefit--relax { top: 528px; }
  .promo {
    position: absolute; left: 566px; top: 418px; width: 136px;
    text-align: center; color: var(--brown-text);
  }
  .promo-label {
    font-family: "Poppins", sans-serif; font-weight: 600;
    font-size: 12px; line-height: 15px; color: var(--orange); letter-spacing: 0.5px;
  }
  .promo-price {
    font-family: "Poppins", sans-serif; font-weight: 600;
    font-size: 42px; line-height: 48px; color: var(--brown-text);
  }
  .promo-text { font-size: 12.5px; line-height: 15px; }
  .map {
    position: absolute; left: 23px; top: 666px; width: 344px; height: 296px;
    border: 5px solid var(--map-orange); border-radius: 10px;
    background: linear-gradient(160deg, var(--map-yellow), var(--map-orange));
  }
  .brand {
    position: absolute; left: 400px; top: 772px; width: 280px;
    display: flex; align-items: center; justify-content: center; gap: 10px;
    font-family: "Poppins", sans-serif; font-weight: 600; font-size: 30px; line-height: 40px; color: var(--white);
  }
  .brand-dot { width: 16px; height: 16px; border-radius: 50%; background: var(--orange); }
  .contact {
    position: absolute; left: 395px; width: 290px; text-align: center;
    font-family: "Arimo", Arial, sans-serif; font-weight: 700; color: var(--white);
  }
  .contact--address { top: 824px; font-size: 18px; line-height: 24px; }
  .contact--phone { top: 896px; font-size: 42px; line-height: 48px; }
  .contact--email { top: 946px; font-size: 18px; line-height: 22px; }
</style>
</head>
<body>
<main class="flyer">
  <svg class="decor" viewBox="0 0 707 1004" aria-hidden="true">
    <circle cx="645" cy="495" r="100" fill="var(--peach)"/>
    <circle cx="720" cy="735" r="120" fill="none" stroke="var(--peach)" stroke-width="34"/>
  </svg>

  <h1 class="headline">How does a Massage<br>benefit us?</h1>

  <section class="benefit benefit--sports">
    <h2>Sports massage</h2>
    <p>Remain injury free &amp; improve your performance by assisting<br>muscles back to their normal resting length therefore improving<br>strength and flexibility.<br>
    Deep tissue massage to realign muscle fibres and eliminate trigger<br>points. Speed up your recovery between training sessions and<br>events by flushing out metabolic waste.</p>
  </section>

  <section class="benefit benefit--remedial">
    <h2>Therapeutic/remedial massage</h2>
    <p>Reduce the incidence of headaches and migraines.<br>
    Resolve your lower back pain.<br>
    Improve your posture and become pain-free.<br>
    Eliminate "mouse" shoulder and neck pain from poor<br>desk posture.<br>
    Eliminate referral pain such as Sciatica and arm pain.</p>
  </section>

  <section class="benefit benefit--relax">
    <h2>Relaxation massage</h2>
    <p>Scheduled time-out for you.<br>
    De-stress and reduce your muscle tension.<br>
    Quieten your mind and assist in a good night’s sleep.</p>
  </section>

  <aside class="promo">
    <p class="promo-label">LUNCH-BREAK OFFER</p>
    <p class="promo-price">$20</p>
    <p class="promo-text">Professional quick de-stress relaxation massage for office workers</p>
  </aside>

  <svg class="decor" viewBox="0 0 707 1004" aria-hidden="true">
    <path d="M0 706 C 200 688, 480 700, 707 772 L707 1004 L0 1004 Z" fill="var(--brown)"/>
    <path d="M0 706 C 200 688, 480 700, 707 772" fill="none" stroke="var(--orange-line)" stroke-width="4"/>
  </svg>

  <div class="map" role="img" aria-label="Street map showing the way to the shop, with the nearby car park and main roads"></div>

  <div class="brand"><span class="brand-dot"></span>Lotus Vale</div>

  <p class="contact contact--address">7, 41 - 55 Brindlecombe Road,<br>Takapuna, Auckland</p>
  <p class="contact contact--phone">09-5317208</p>
  <p class="contact contact--email">lotusvale.nz@examplemail.com</p>
</main>
</body>
</html>
```